Business cards for Marrowfield Consulting with the following info for the front side:

Marrowfield Consulting
Executive Coaching and Human Capital Strategy
www.marrowfield.example

Idalia Renvoort
Principal
idalia@marrowfield.example
+1 555 274 9186

Black background, text using the colours of the logo - enclosed.

The back side of the business card should feature the logo in the middle, with "Executive Coaching and Human Capital Strategy" on top and "www.marrowfield.example" below.

```html
<!DOCTYPE html>
<html lang="en">
<head>
<meta charset="utf-8">
<title>Marrowfield Consulting — Business Cards</title>
<link rel="stylesheet" href="https://fonts.googleapis.com/css2?family=Montserrat:wght@400;500;700&display=swap">
<style>
  :root {
    --canvas: #d6d6d6;
    --card: #060606;
    --brand-blue: #1f9fcb;
    --brand-yellow: #f1b80d;
    --mark-fill: #123847;
    --text-light: #f2f2f2;
  }
  * { box-sizing: border-box; margin: 0; padding: 0; }
  html, body {
    width: 1200px; height: 1021px; overflow: hidden;
    background: var(--canvas);
    font-family: "Montserrat", sans-serif;
  }
  .sheet { position: relative; width: 1200px; height: 1021px; }
  .card {
    position: absolute; left: 220px;
    width: 760px; height: 434px;
    background: var(--card);
    border-radius: 4px;
    box-shadow: 0 12px 30px rgba(0,0,0,0.35);
    overflow: hidden;
  }
  .card--back { top: 48px; }
  .card--front { top: 538px; }

  .mark-area {
    position: absolute;
    border-radius: 50%;
    background: var(--mark-fill);
  }
  .card--back .mark-area { left: -150px; top: -80px; width: 460px; height: 460px; }
  .card--front .mark-area { left: 530px; top: 70px; width: 430px; height: 430px; }

  .wordmark {
    display: flex; align-items: center; gap: 12px;
    color: var(--brand-blue);
    font-weight: 500;
    letter-spacing: 1.5px;
    line-height: 1;
    white-space: nowrap;
  }
  .wordmark__dot {
    width: 46px; height: 46px; border-radius: 50%;
    background: var(--brand-blue);
    flex: none;
  }
  .tagline {
    color: var(--text-light);
    letter-spacing: 0.4px;
    white-space: nowrap;
  }

  /* back side */
  .card--back .brand { position: absolute; left: 345px; top: 160px; }
  .card--back .wordmark { font-size: 40px; }
  .card--back .tagline { margin-top: 10px; font-size: 14px; }
  .card--back .site {
    position: absolute; left: 420px; top: 318px;
    color: var(--brand-blue);
    font-size: 16px; letter-spacing: 0.5px;
  }

  /* front side */
  .card--front .brand { position: absolute; left: 52px; top: 46px; }
  .card--front .wordmark { font-size: 36px; }
  .card--front .tagline { margin: 6px 0 0 58px; font-size: 12.5px; }

  .person { position: absolute; left: 68px; top: 160px; }
  .person__name {
    color: var(--brand-blue);
    font-weight: 700; font-size: 22px; letter-spacing: 0.6px;
  }
  .person__role { color: var(--text-light); font-size: 17px; margin-top: 2px; }

  .contacts { position: absolute; left: 68px; top: 262px; list-style: none; }
  .contacts li {
    display: flex; align-items: center; gap: 10px;
    color: var(--text-light);
    font-size: 18px; line-height: 27px;
    letter-spacing: 0.3px;
  }
  .contacts svg {
    width: 16px; height: 16px; flex: none;
    stroke: var(--brand-yellow); fill: none; stroke-width: 1.8;
  }
</style>
</head>
<body>
<main class="sheet">

  <section class="card card--back" aria-label="Card back">
    <div class="mark-area" role="img" aria-label="Large brand mark decoration"></div>
    <div class="brand">
      <div class="wordmark">MARROWFIELD</div>
      <p class="tagline">Executive Coaching &amp; Human Capital Strategy</p>
    </div>
    <p class="site">www.marrowfield.example</p>
  </section>

  <section class="card card--front" aria-label="Card front">
    <div class="mark-area" role="img" aria-label="Large brand mark decoration"></div>
    <div class="brand">
      <div class="wordmark"><span class="wordmark__dot"></span>MARROWFIELD</div>
      <p class="tagline">Executive Coaching &amp; Human Capital Strategy</p>
    </div>

    <div class="person">
      <p class="person__name">Idalia Renvoort</p>
      <p class="person__role">Principal</p>
    </div>

    <ul class="contacts">
      <li>
        <svg viewBox="0 0 16 16" aria-hidden="true"><path d="M3 1.5h3l1 3.5-2 1.2a8 8 0 0 0 4.8 4.8L11 9l3.5 1v3a1.5 1.5 0 0 1-1.5 1.5A11.5 11.5 0 0 1 1.5 3 1.5 1.5 0 0 1 3 1.5z"/></svg>
        +1 555 274 9186
      </li>
      <li>
        <svg viewBox="0 0 16 16" aria-hidden="true"><rect x="1.5" y="3.5" width="13" height="9"/><path d="M1.5 3.5 8 9l6.5-5.5"/></svg>
        idalia@marrowfield.example
      </li>
      <li>
        <svg viewBox="0 0 16 16" aria-hidden="true"><circle cx="8" cy="8" r="6.5"/><ellipse cx="8" cy="8" rx="3" ry="6.5"/><path d="M1.5 8h13"/></svg>
        www.marrowfield.example
      </li>
    </ul>
  </section>

</main>
</body>
</html>
```